Industrial Project Sign

We need an eye catching (but professional) industrial project sign that will be very large (roughly 12' high x 18' wide). This sign will be highly visible from the adjacent high speed highway.

* The following needs to be at the bottom of the signage: Logo (uploaded), Name (Pillar Ventures Group, Inc.) (uploaded) and phone number (555)613-8874

*Name of Project - "Brambleford Industrial Center"

* Text items
Land for Sale
Build to Suit
Zoning: Industrial (G I & L I)

* Interesting background that is eye catching
Updates

Good morning all,

We are considering all designers options as we go and are waiting for the final designs to come in by the 4th so that we can give each one a good look.   If you have any new designs, questions, further design options or any tweeks you want to do to current designs, please do so at this time.

Thanks to all of you for your submissions.

Industry/Entity Type

Industrial

```html
<!DOCTYPE html>
<html lang="en">
<head>
<meta charset="utf-8">
<title>Brambleford Industrial Center – Site Sign</title>
<link rel="stylesheet" href="https://fonts.googleapis.com/css2?family=Arimo:wght@700&display=swap">
<style>
  :root {
    --brand-red: #6b0000;
    --text-grey: #5c5656;
    --white: #ffffff;
    --roof-steel: #6f7378;
    --wall-grey: #8e949c;
    --floor-light: #d6d8da;
    --floor-bright: #e9eaeb;
  }
  * { margin: 0; padding: 0; box-sizing: border-box; }
  html, body { width: 1200px; height: 675px; overflow: hidden; background: #ffffff; }
  .sign {
    position: relative;
    width: 1200px;
    height: 675px;
    overflow: hidden;
    font-family: "Arimo", Arial, sans-serif;
    font-weight: 700;
  }
  .sign__backdrop {
    position: absolute;
    inset: 0;
    background: linear-gradient(180deg,
      var(--roof-steel) 0%,
      #868a90 22%,
      var(--wall-grey) 40%,
      #a9adb2 52%,
      var(--floor-light) 66%,
      var(--floor-bright) 82%,
      #cfd1d3 100%);
  }
  .offer-panel {
    position: absolute;
    left: 702px;
    top: 11px;
    width: 488px;
    height: 117px;
    background: var(--brand-red);
    padding: 6px 0 0 7px;
    color: var(--text-grey);
    font-size: 34px;
    line-height: 33px;
    letter-spacing: 0.2px;
  }
  .feature-frame {
    position: absolute;
    left: 432px;
    top: 184px;
    width: 380px;
    height: 348px;
    filter: drop-shadow(2px 4px 4px rgba(0,0,0,0.35));
  }
  .project-title {
    position: absolute;
    left: 440px;
    top: 200px;
    width: 370px;
    text-align: right;
    color: var(--white);
    font-size: 55px;
    line-height: 48px;
    letter-spacing: -0.5px;
    text-shadow: 1px 2px 3px rgba(0,0,0,0.3);
  }
  .project-title span { display: block; }
  .project-title .line-1 { padding-right: 4px; }
  .project-title .line-2 { padding-right: 6px; }
  .company-mark {
    position: absolute;
    left: 20px;
    top: 548px;
    width: 100px;
    text-align: center;
    color: var(--brand-red);
    font-size: 22px;
  }
  .company-mark .mark-square,
  .corner-mark .mark-square {
    display: block;
    margin: 0 auto 6px;
    width: 50px;
    height: 50px;
    background: var(--brand-red);
  }
  .company-name {
    position: absolute;
    left: 148px;
    top: 572px;
    color: var(--brand-red);
    font-size: 20px;
  }
  .company-rule {
    position: absolute;
    left: 134px;
    top: 601px;
    width: 291px;
    height: 3px;
    background: var(--brand-red);
  }
  .phone {
    position: absolute;
    left: 612px;
    top: 575px;
    color: var(--white);
    font-size: 35px;
    letter-spacing: 0.3px;
    text-shadow: 1px 1px 2px rgba(0,0,0,0.2);
  }
  .corner-mark {
    position: absolute;
    left: 1076px;
    top: 548px;
    width: 118px;
    text-align: center;
    color: var(--brand-red);
    font-size: 24px;
  }
</style>
</head>
<body>
  <main class="sign">
    <div class="sign__backdrop" role="img" aria-label="Photograph of a large empty warehouse interior with steel roof trusses, hanging lights and a polished concrete floor"></div>

    <section class="offer-panel">
      <p>land for sale</p>
      <p>build to suit</p>
      <p>zoning: industrial (GI &amp; LI)</p>
    </section>

    <svg class="feature-frame" viewBox="0 0 380 348" aria-hidden="true">
      <polyline points="256,6 6,6 6,342 374,342 374,240" fill="none" stroke="#ffffff" stroke-width="12" stroke-linecap="square"/>
    </svg>

    <h1 class="project-title">
      <span class="line-1">brambleford</span>
      <span class="line-2">industrial</span>
      <span class="line-3">center</span>
    </h1>

    <div class="company-mark">
      <span class="mark-square"></span>
      pillar
    </div>
    <p class="company-name">pillar ventures group inc</p>
    <div class="company-rule"></div>

    <p class="phone">(555)613-8874</p>

    <div class="corner-mark">
      <span class="mark-square"></span>
      PILLAR
    </div>
  </main>
</body>
</html>
```